Hair and Wellness Brochure and Pricelist design

I am requiring a brochure that has a fresh, though alternative design. My business name is The Quiet Harbor Hair and Wellness. I have a very professional approach to my work and love to give that little bit extra to all of my clients. My passion for health, has led me to channel my business alternatively by using non toxic colours and styling products and through that same vein, I have studied Aromatherapy, Indian Head Massage and Reiki...all additional services I use where required.
My studio has very neutral tones of beige,white and beech wood but these tones aren't necessarily required for the brochure.I like to create a space of calm, peace and quiet, where my clients feel refreshed and rejuvenated..

```html
<!DOCTYPE html>
<html lang="en">
<head>
<meta charset="utf-8">
<title>The Quiet Harbor Hair and Wellness — Price List</title>
<link href="https://fonts.googleapis.com/css2?family=Ubuntu:wght@400&display=swap" rel="stylesheet">
<style>
  :root {
    --cream: #f5f2dc;
    --cream-deep: #ebe6ca;
    --taupe: #7d6b5b;
    --taupe-soft: #a39382;
    --taupe-light: #c4b7a6;
    --ornament: #8c7b6b;
    --label: #f4efe0;
  }
  html, body {
    margin: 0;
    padding: 0;
    overflow: hidden;
  }
  .canvas {
    position: relative;
    width: 1200px;
    height: 2770px;
    overflow: hidden;
    background: var(--cream);
    font-family: "Ubuntu", "Helvetica Neue", Arial, sans-serif;
  }
  .floral-pattern {
    position: absolute;
    inset: 0;
    background:
      radial-gradient(circle at 20% 35%, var(--cream-deep) 0%, rgba(235,230,202,0) 18%),
      radial-gradient(circle at 80% 55%, var(--cream-deep) 0%, rgba(235,230,202,0) 18%),
      radial-gradient(circle at 30% 78%, var(--cream-deep) 0%, rgba(235,230,202,0) 16%),
      radial-gradient(circle at 85% 15%, var(--cream-deep) 0%, rgba(235,230,202,0) 16%),
      var(--cream);
  }
  .swirl-ornament {
    position: absolute;
    left: 0;
    top: 0;
    width: 880px;
    height: 700px;
  }
  .price-list {
    position: absolute;
    left: 162px;
    top: 0;
    width: 914px;
    margin: 0;
    padding: 0;
    list-style: none;
  }
  .price-item {
    position: absolute;
    left: 0;
    width: 914px;
    display: flex;
    flex-direction: column;
    align-items: center;
    justify-content: center;
    text-align: center;
    background: var(--taupe);
    border-radius: 18px;
    box-shadow: 0 6px 10px rgba(80,64,50,0.25);
    color: var(--label);
    font-size: 48px;
    line-height: 1.3;
  }
  .price-item .service { display: block; padding: 0 80px; }
  .price-item .price { display: block; }
  .item-shampoo { top: 986px; height: 236px; }
  .item-hot-tool { top: 1318px; height: 286px; }
  .item-cut { top: 1690px; height: 246px; }
  .item-mens { top: 2058px; height: 242px; }
  .footer-waves {
    position: absolute;
    left: 0;
    bottom: 0;
    width: 1200px;
    height: 420px;
  }
</style>
</head>
<body>
<main class="canvas">
  <div class="floral-pattern" role="img" aria-label="Faint outline lily flower pattern across the background"></div>

  <svg class="swirl-ornament" viewBox="0 0 880 700" role="img" aria-label="Flowing taupe swirl ornament in the top left corner">
    <defs>
      <linearGradient id="swirl-tone" x1="0" y1="0" x2="1" y2="1">
        <stop offset="0" stop-color="var(--ornament)" stop-opacity="0.55"/>
        <stop offset="0.55" stop-color="var(--ornament)" stop-opacity="0.28"/>
        <stop offset="1" stop-color="var(--ornament)" stop-opacity="0.05"/>
      </linearGradient>
    </defs>
    <path d="M0 0 L620 0 C 700 120, 860 300, 870 560 C 760 660, 540 690, 380 640 C 220 600, 80 660, 0 690 Z" fill="url(#swirl-tone)"/>
  </svg>

  <ul class="price-list">
    <li class="price-item item-shampoo">
      <span class="service">Shampoo &amp; blow dry</span>
      <span class="price">$40</span>
    </li>
    <li class="price-item item-hot-tool">
      <span class="service">Hot tool styling with Shampoo included</span>
      <span class="price">$50</span>
    </li>
    <li class="price-item item-cut">
      <span class="service">Shampoo cut &amp; blow dry</span>
      <span class="price">$70</span>
    </li>
    <li class="price-item item-mens">
      <span class="service">Men's style cut</span>
      <span class="price">$30</span>
    </li>
  </ul>

  <svg class="footer-waves" viewBox="0 0 1200 420" aria-hidden="true">
    <path d="M0 140 C 300 60, 800 40, 1200 70 L1200 420 L0 420 Z" fill="var(--taupe-light)"/>
    <path d="M0 190 C 350 110, 800 100, 1200 130 L1200 420 L0 420 Z" fill="var(--taupe-soft)"/>
    <path d="M0 260 C 350 180, 800 170, 1200 200 L1200 420 L0 420 Z" fill="var(--taupe)"/>
  </svg>
</main>
</body>
</html>
```